Company Broshure Oil&Energy Industry

We have recently completed a company rebranding, and our new website is now fully live and available at www.velmorquist.ro.

To ensure consistency across all communication materials, we would like to redesign our company presentation flyer/brochure so that it fully reflects the updated branding and visual identity of the website.

Please find attached our current brochure (last item uploaded on the list), which should be redesigned in line with the new website’s look and feel. The overall structure and text content should remain unchanged; only the layout and visual design need to be updated. I have uploaded pictures from of the website theme. Can be used by designers for the new design.
Updates

We uploaded pictures belonging to website design theme that can be used for the new brochure.

Target Market(s)

EPC Contractors

Industry/Entity Type

Oil&Energy

Font styles to use
Other font styles liked:
• Calibri

Colors
0094D4
00A9DD
6FCCEA
C7EBF8
E9F6FB

Requirements
Must have
• a clear structure, elegant layout
Nice to have
• I would like to have a dynamic approach. To feel elegant and alive.

```html
<!DOCTYPE html>
<html lang="en">
<head>
<meta charset="utf-8">
<title>Velmorquist Group – Company Brochure</title>
<link rel="stylesheet" href="https://fonts.googleapis.com/css2?family=Arimo:wght@400;700&family=Carlito:ital,wght@0,400;1,400&display=swap">
<style>
  :root{
    --backdrop:#a3a3a3;
    --paper:#ffffff;
    --navy:#34465f;
    --navy-deep:#26354a;
    --navy-soft:#4a5d78;
    --ink:#111111;
    --brand:#e0742a;
    --steel-light:#e4e6e9;
    --steel-mid:#c9ccd1;
    --sky:#c7d6e4;
  }
  *{margin:0;padding:0;box-sizing:border-box}
  html,body{width:888px;height:1200px;overflow:hidden;background:var(--backdrop)}
  body{position:relative;font-family:"Carlito",Calibri,sans-serif;color:var(--ink)}
  .page{position:absolute;width:380px;height:537px;background:var(--paper);overflow:hidden;box-shadow:6px 6px 10px rgba(0,0,0,.35)}
  .page--cover{left:45px;top:47px}
  .page--about{left:462px;top:47px}
  .page--services{left:45px;top:617px}
  .page--contact{left:462px;top:617px}
  .abs{position:absolute}
  .navy-block{position:absolute;background:linear-gradient(180deg,var(--navy-deep),var(--navy-soft))}
  .photo{position:absolute}
  .brand{position:absolute;display:flex;align-items:center;gap:7px;font-family:"Arimo",Arial,sans-serif;font-weight:700;color:var(--brand);white-space:nowrap}
  .brand__mark{display:block;background:var(--brand)}
  .heading{position:absolute;font-family:"Arimo",Arial,sans-serif;font-weight:700;letter-spacing:.5px}
  .tagline{position:absolute;left:28px;top:508px;font-family:"Arimo",Arial,sans-serif;font-style:italic;font-size:11px}
  .body-copy{position:absolute;font-size:10.2px;line-height:12.4px}
  .body-copy p{margin-bottom:11px}
  .service-list{position:absolute;left:29px;top:303px;width:330px;list-style:none;font-size:11px;line-height:14px}
  .service-list li{position:relative;padding-left:22px}
  .service-list li::before{content:"•";position:absolute;left:0}
  .contact-lines{position:absolute;left:27px;top:250px;color:#fff;font-size:11.3px;line-height:17.5px}
</style>
</head>
<body>

<section class="page page--cover">
  <div class="photo" role="img" aria-label="Workers in safety gear climbing a staircase on a white storage tank" style="left:0;top:141px;width:380px;height:396px;background:linear-gradient(160deg,var(--steel-light),#d6d8dc 60%,#c3c6cb)"></div>
  <div class="navy-block" style="left:255px;top:0;width:86px;height:213px"></div>
  <div class="brand" style="left:30px;top:58px;font-size:15px"><span class="brand__mark" style="width:14px;height:14px"></span>Velmorquist Group</div>
  <h1 class="heading" style="left:29px;top:376px;font-size:37px;line-height:39px;color:var(--navy)">VELMORQUIST<br>GROUP</h1>
  <p class="tagline" style="color:#fff">Your Valuable Partner for Oil &amp;Energy Projects</p>
</section>

<section class="page page--about">
  <div class="photo" role="img" aria-label="Engineer in an orange hard hat looking at scaffolding" style="left:148px;top:0;width:232px;height:238px;background:linear-gradient(135deg,#d9e2ea,#b9c3cc 55%,#8a8f7a)"></div>
  <div class="navy-block" style="left:0;top:200px;width:324px;height:68px;background:linear-gradient(90deg,var(--navy-deep),var(--navy-soft))"></div>
  <div class="brand" style="left:30px;top:50px;font-size:13px"><span class="brand__mark" style="width:12px;height:12px"></span>Velmorquist Group</div>
  <h2 class="heading" style="left:27px;top:292px;font-size:37px;color:#000">WHO WE ARE</h2>
  <div class="body-copy" style="left:27px;top:348px;width:330px">
    <p>Velmorquist Group is a Romanian registred company, founded in 2003.</p>
    <p>We have been active in Oil&amp;Energy industry serving local and international market by sourcing highly specilised professionals for Oil &amp; Energy projects.</p>
    <p>We offer a wide range of services that encompass every stage of the process, starting from the initial selection of professionals and extending to the management of employment and logistics (mobilisation) for the assigned resources. Whether the project is located domestically or abroad, we offer tailored support to ensure successful project completion for our clients.</p>
  </div>
  <p class="tagline" style="color:#111">Your Valuable Partner for Oil &amp;Energy Projects</p>
</section>

<section class="page page--services">
  <div class="photo" role="img" aria-label="Engineer in a white hard hat reading plans in front of a refinery" style="left:0;top:0;width:380px;height:249px;background:linear-gradient(110deg,#6f8a9e,#a9b8c4 45%,#e9e2d8 75%,#f2ede6)"></div>
  <div class="brand" style="left:286px;top:24px;font-size:8px;gap:4px"><span class="brand__mark" style="width:7px;height:7px"></span>Velmorquist Group</div>
  <div class="navy-block" style="left:18px;top:223px;width:221px;height:67px;background:linear-gradient(90deg,var(--navy-deep),var(--navy-soft))"></div>
  <h2 class="heading" style="left:29px;top:234px;font-size:38px;color:#fff">SERVICES</h2>
  <ul class="service-list">
    <li>Discipline Site Supervision (mechanical, electric, I&amp;C, piping)</li>
    <li>Site Management (Construction/Commissioning)</li>
    <li>Project Service Management (Planning, Cost Control/Estimate, Project Control, Document Controlling, Contract Control, Procurement)</li>
    <li>Quality Control, Quality Assurance</li>
    <li>HSE supervision, HSE Management</li>
    <li>Welding &amp; NDT inspections</li>
    <li>Discipline Engineering (process, piping, stress piping, instrument, electric, civil)</li>
  </ul>
  <p class="tagline" style="color:#111">Your Valuable Partner for Oil &amp;Energy Projects</p>
</section>

<section class="page page--contact">
  <div class="photo" role="img" aria-label="Woman working on a laptop in a bright office" style="left:0;top:249px;width:380px;height:288px;background:linear-gradient(120deg,#5b5a58,#9a8f80 45%,#d9d6d0 75%,#eeeae4)"></div>
  <div class="navy-block" style="left:329px;top:0;width:30px;height:99px"></div>
  <div class="brand" style="left:33px;top:62px;font-size:17px"><span class="brand__mark" style="width:16px;height:16px"></span>Velmorquist Group</div>
  <div class="navy-block" style="left:0;top:156px;width:289px;height:189px;background:linear-gradient(135deg,var(--navy-deep),var(--navy-soft))"></div>
  <h2 class="heading" style="left:27px;top:184px;font-size:38px;color:#fff">CONTACT</h2>
  <div class="contact-lines">
    <div>0040721000457</div>
    <div>office@velmorquist.ro</div>
    <div>www.velmorquist.ro</div>
    <div>Str. Fabricii, no.7 Bucharest, Romania</div>
  </div>
  <p class="tagline" style="color:#fff">Your Valuable Partner for Oil &amp;Energy Projects</p>
</section>

</body>
</html>
```